Elementary School Profile of a Falconet

Please recreate a poster of our Profile of a Falconet traits that we desire to have when they graduate from 4th grade. This should be kid-friendly and kid-themed with icons to help communicate the Competencies. See attached six competencies and the "I can" statements next to. Our colors are navy, red and white. Our logo is attached as well. This will be made into a poster and displayed in each classroom, the office, and also used on social media.

```html
<!DOCTYPE html>
<html lang="en">
<head>
<meta charset="utf-8">
<title>Profile of a Falconet – Early Learners and Elementary School</title>
<link rel="stylesheet" href="https://fonts.googleapis.com/css2?family=Montserrat:wght@600;800&family=Ubuntu:wght@400;500;700&display=swap">
<style>
  :root {
    --navy: #0d0f4a;
    --red: #a50d0d;
    --cream: #fffde8;
    --white: #ffffff;
    --ink: #12143f;
    --backdrop: #ececec;
  }
  * { box-sizing: border-box; margin: 0; padding: 0; }
  html, body {
    width: 978px; height: 1200px; overflow: hidden;
    background: var(--backdrop);
  }
  .poster {
    position: absolute; left: 65px; top: 0;
    width: 848px; height: 1200px;
    background: var(--white);
    font-family: "Ubuntu", sans-serif;
    color: var(--ink);
  }
  .brand {
    position: absolute; left: 14px; top: 40px;
    width: 172px; height: 48px;
    display: flex; align-items: center; gap: 8px;
  }
  .brand-dot { width: 26px; height: 26px; border-radius: 50%; background: var(--navy); flex: none; }
  .brand-name { font-weight: 700; font-size: 24px; color: var(--red); }

  .masthead {
    position: absolute; left: 201px; top: 11px; right: 0; height: 110px;
    border-radius: 26px 0 0 26px; overflow: hidden;
    text-align: center;
  }
  .masthead-top {
    height: 74px; background: var(--navy); color: var(--white);
    padding-top: 9px;
  }
  .district {
    font-family: "Montserrat", sans-serif; font-weight: 600;
    font-size: 12px; letter-spacing: 5.2px;
  }
  .title {
    font-family: "Montserrat", sans-serif; font-weight: 800;
    font-size: 38.5px; line-height: 44px; letter-spacing: 0.2px;
  }
  .masthead-band {
    height: 36px; background: var(--red); color: var(--white);
    font-family: "Montserrat", sans-serif; font-weight: 800;
    font-size: 19.5px; line-height: 36px; letter-spacing: 0.3px;
  }

  .tab {
    position: absolute; left: 29px; top: 135px; width: 191px; height: 60px;
    background: var(--red); color: var(--white);
    border-radius: 18px 18px 0 0;
    font-family: "Montserrat", sans-serif; font-weight: 800; font-size: 20px;
    padding: 15px 0 0 19px; letter-spacing: 0.3px;
  }
  .matrix {
    position: absolute; left: 29px; top: 186px; width: 787px; height: 984px;
    border: 3px solid var(--navy); border-radius: 18px; overflow: hidden;
    background: var(--white);
  }
  .competency {
    display: grid;
    grid-template-columns: 187px 351px 1fr;
    border-top: 2px solid var(--navy);
  }
  .competency:first-child { border-top: none; }
  .competency-name {
    grid-column: 1; grid-row: 1 / -1;
    border-right: 2px solid var(--navy);
    color: var(--red); font-weight: 500; font-size: 20px; line-height: 28px;
    padding: 12px 0 0 18px;
    background: var(--white);
  }
  .statement, .mark {
    border-top: 1px solid var(--navy);
  }
  .statement {
    grid-column: 2; border-right: 2px solid var(--navy);
    position: relative; padding: 9px 6px 0 25px;
    font-size: 14.4px; line-height: 18px;
  }
  .statement::before {
    content: ""; position: absolute; left: 10px; top: 14px;
    border-left: 6px solid var(--red);
    border-top: 3.5px solid transparent; border-bottom: 3.5px solid transparent;
  }
  .mark { grid-column: 3; }
  .first { border-top: none; }
  .cream { background: var(--cream); }
</style>
</head>
<body>
<main class="poster">
  <div class="brand"><span class="brand-dot"></span><span class="brand-name">Falconets</span></div>

  <header class="masthead">
    <div class="masthead-top">
      <div class="district">MAPLE HOLLOW PUBLIC SCHOOLS</div>
      <h1 class="title">PROFILE OF A FALCONET</h1>
    </div>
    <div class="masthead-band">EARLY LEARNERS AND ELEMENTARY SCHOOL</div>
  </header>

  <div class="tab">COMPETENCY</div>

  <section class="matrix">
    <div class="competency" style="grid-template-rows:65px 65px 52px">
      <h2 class="competency-name">Communicator</h2>
      <p class="statement first cream">I can use words, writing, and<br>pictures to clearly share ideas.</p><div class="mark first cream"></div>
      <p class="statement">I can look at the speaker and listen<br>carefully to understand what they<br>are saying.</p><div class="mark"></div>
      <p class="statement cream">I know how to adjust my communication<br>for different places and people.</p><div class="mark cream"></div>
    </div>
    <div class="competency" style="grid-template-rows:59px 55px 54px">
      <h2 class="competency-name">Critical<br>Thinker</h2>
      <p class="statement first">I can ask questions like "why" and "how"<br>to learn more about the world.</p><div class="mark first"></div>
      <p class="statement cream">When faced with a problem, I can be creative<br>and come up with different solutions.</p><div class="mark cream"></div>
      <p class="statement">I can use facts and clues to help make<br>wise decisions.</p><div class="mark"></div>
    </div>
    <div class="competency" style="grid-template-rows:58px 50px 53px">
      <h2 class="competency-name">Responsible</h2>
      <p class="statement first cream">I can take ownership of my actions and<br>remember to complete my job.</p><div class="mark first cream"></div>
      <p class="statement">I can take care of my belongings and<br>always try my best in schoolwork.</p><div class="mark"></div>
      <p class="statement cream">I can tell the truth and act with integrity<br>even when no one is watching.</p><div class="mark cream"></div>
    </div>
    <div class="competency" style="grid-template-rows:58px 47px 53px">
      <h2 class="competency-name">Adaptable</h2>
      <p class="statement first">When a plan changes or a task is hard,<br>I can stay calm and try a new way.</p><div class="mark first"></div>
      <p class="statement cream">I can learn from mistakes and use past<br>knowledge to try new things.</p><div class="mark cream"></div>
      <p class="statement">I can work and play well with people<br>who are different from me.</p><div class="mark"></div>
    </div>
    <div class="competency" style="grid-template-rows:51px 52px 49px">
      <h2 class="competency-name">Collaborator</h2>
      <p class="statement first cream">I can share ideas and work together<br>with a group to reach a common goal.</p><div class="mark first cream"></div>
      <p class="statement">I can listen to my teammates and<br>respect their different ideas.</p><div class="mark"></div>
      <p class="statement cream">I can know when to share, when to<br>help others, and when to be the leader.</p><div class="mark cream"></div>
    </div>
    <div class="competency" style="grid-template-rows:52px 49px 59px">
      <h2 class="competency-name">Compassionate</h2>
      <p class="statement first">I can be empathetic, noticing how others<br>are feeling (happy, sad, frustrated).</p><div class="mark first"></div>
      <p class="statement cream">I can use kind words and gentle actions<br>to support their friends.</p><div class="mark cream"></div>
      <p class="statement">I can look for ways to help their school<br>and the community.</p><div class="mark"></div>
    </div>
  </section>
</main>
</body>
</html>
```